salami paper bag design The size is 10.5cm 21.5cm 6.7cm

This time we need to make renew salami package design. Planning to make paper salami package. I tried to design but I couldnt formyself.
So please correct my design and recreate more nicer package design from my salami design that attach on the documents.
Logo part I am planning gold stamp. If anybody can make more nicer logo for the package,I don’t mind it.please change the color and shape and everything.
The size is 10.5cm 21.5cm 6.7cm
Thank you.

Target Market(s)

uper market make costomer feel luxurious

Industry/Entity Type

salami matured meat products

Font styles to use
Sans Serif
Decorative
Script

Colors

Designer to choose colors to be used in the design.

Requirements
Nice to have
• Make customer feel joy for genuine fermented salami with wine
Should not have
• My projrct must not have cheap discount design.

```html
<!DOCTYPE html>
<html lang="en">
<head>
<meta charset="utf-8">
<title>Corvani salami box dieline</title>
<link href="https://fonts.googleapis.com/css2?family=Libre+Caslon+Text:wght@400;700&family=Pinyon+Script&display=swap" rel="stylesheet">
<style>
  :root {
    --backdrop: #433e3b;
    --frame-line: #8a8581;
    --olive: #969a3a;
    --night: #07060c;
    --gold: #e0b02c;
    --ink: #111010;
    --serif: "Libre Caslon Text", Georgia, serif;
    --script: "Pinyon Script", cursive;
  }
  html, body { margin: 0; padding: 0; overflow: hidden; background: var(--backdrop); }
  .canvas { width: 1004px; height: 1200px; display: block; }
  .backdrop { fill: var(--backdrop); stroke: var(--frame-line); stroke-width: 1.5; }
  .panel-olive { fill: var(--olive); }
  .panel-night { fill: var(--night); }
  .brand { font-family: var(--serif); font-weight: 700; }
  .brand-gold { fill: var(--gold); }
  .brand-ink { fill: var(--ink); }
  .small-serif { font-family: var(--serif); font-weight: 400; }
  .tagline { font-family: var(--script); fill: var(--ink); }
  .vent-hole { fill: none; stroke: #c9cb8f; stroke-width: 1; }
  .window-frame { fill: none; stroke: var(--gold); stroke-width: 5; }
  .window-inner { fill: none; stroke: var(--night); stroke-width: 1.5; }
</style>
</head>
<body>
<svg class="canvas" viewBox="0 0 1004 1200" xmlns="http://www.w3.org/2000/svg">
  <defs>
    <linearGradient id="ornament-olive" x1="0" y1="0" x2="1" y2="1">
      <stop offset="0" stop-color="#7f8330"/>
      <stop offset="1" stop-color="#6e7029"/>
    </linearGradient>
    <radialGradient id="ornament-gold" cx="0.5" cy="0.5" r="0.6">
      <stop offset="0" stop-color="#4a3c14"/>
      <stop offset="1" stop-color="#15120c"/>
    </radialGradient>
    <linearGradient id="salami-photo" x1="0" y1="0" x2="1" y2="1">
      <stop offset="0" stop-color="#ece7dc"/>
      <stop offset="0.6" stop-color="#d8cfc0"/>
      <stop offset="1" stop-color="#b9a696"/>
    </linearGradient>
    <path id="quality-arc" d="M448 448 Q502 430 556 448"/>
  </defs>

  <rect class="backdrop" x="0.75" y="0.75" width="1002.5" height="1198.5"/>

  <!-- Top flap (printed upside down) -->
  <rect class="panel-olive" x="358" y="102" width="288" height="187"/>
  <g class="flap-top" transform="rotate(180 502 195)">
    <text class="brand brand-ink" x="502" y="172" font-size="36" text-anchor="middle">Corvani</text>
    <text class="tagline" x="502" y="192" font-size="20" text-anchor="middle">Artisan</text>
    <rect role="img" aria-label="Gold sunburst medallion with scrolling flourishes" x="450" y="198" width="104" height="46" rx="8" fill="url(#ornament-olive)"/>
  </g>

  <!-- Left side panel -->
  <rect class="panel-olive" x="169" y="289" width="189" height="621"/>
  <g class="vents-left">
    <circle class="vent-hole" cx="197" cy="320" r="5"/><circle class="vent-hole" cx="197" cy="346" r="5"/>
    <circle class="vent-hole" cx="197" cy="372" r="5"/><circle class="vent-hole" cx="197" cy="398" r="5"/>
    <circle class="vent-hole" cx="197" cy="425" r="5"/><circle class="vent-hole" cx="197" cy="451" r="5"/>
    <circle class="vent-hole" cx="197" cy="477" r="5"/><circle class="vent-hole" cx="197" cy="504" r="5"/>
    <circle class="vent-hole" cx="197" cy="693" r="5"/><circle class="vent-hole" cx="197" cy="719" r="5"/>
    <circle class="vent-hole" cx="197" cy="746" r="5"/><circle class="vent-hole" cx="197" cy="772" r="5"/>
    <circle class="vent-hole" cx="197" cy="798" r="5"/><circle class="vent-hole" cx="197" cy="825" r="5"/>
    <circle class="vent-hole" cx="197" cy="851" r="5"/><circle class="vent-hole" cx="197" cy="877" r="5"/>
  </g>
  <rect role="img" aria-label="Sunburst medallion with scrolling monogram flourish" x="224" y="308" width="95" height="128" rx="10" fill="url(#ornament-olive)"/>
  <rect role="img" aria-label="Sunburst medallion with scrolling monogram flourish" x="224" y="751" width="95" height="129" rx="10" fill="url(#ornament-olive)"/>
  <g class="side-label" transform="translate(271 583) rotate(90)">
    <text class="brand brand-ink" x="0" y="16" font-size="50" text-anchor="middle">Corvani</text>
    <text class="small-serif" x="0" y="-34" font-size="9" fill="var(--ink)" text-anchor="middle" letter-spacing="0.5">SUPERIOR QUALITY</text>
    <text class="small-serif" x="0" y="42" font-size="10" fill="var(--ink)" text-anchor="middle">Since1934</text>
  </g>

  <!-- Front panel -->
  <rect class="panel-night" x="358" y="289" width="288" height="621"/>
  <rect role="img" aria-label="Heraldic crest in red and gold with crown and laurel flourishes" x="432" y="330" width="140" height="76" rx="10" fill="url(#ornament-gold)"/>
  <text class="small-serif" x="502" y="415" font-size="7" fill="var(--gold)" text-anchor="middle">Since1934</text>
  <text class="small-serif" font-size="9" fill="var(--gold)" letter-spacing="0.6"><textPath href="#quality-arc" startOffset="50%" text-anchor="middle">SUPERIOR QUALITY</textPath></text>
  <text class="brand brand-gold" x="502" y="500" font-size="50" text-anchor="middle">Corvani</text>
  <text class="small-serif" x="502" y="521" font-size="10.5" fill="var(--gold)" text-anchor="middle">Since1934</text>

  <g class="product-window">
    <path d="M430 748 V607 Q430 598 439 598 Q446 598 446 590 Q446 553 502 553 Q558 553 558 590 Q558 598 565 598 Q574 598 574 607 V748 Z"
          fill="url(#salami-photo)" role="img" aria-label="Two white-bloomed dry salami sticks seen through the window"/>
    <path class="window-frame" d="M430 748 V607 Q430 598 439 598 Q446 598 446 590 Q446 553 502 553 Q558 553 558 590 Q558 598 565 598 Q574 598 574 607 V748 Z"/>
    <path class="window-inner" d="M435 743 V610 Q435 603 442 603 Q451 603 451 592 Q451 558 502 558 Q553 558 553 592 Q553 603 562 603 Q569 603 569 610 V743 Z"/>
  </g>

  <rect role="img" aria-label="Gold sunburst with monogram scroll flourish" x="438" y="777" width="129" height="95" rx="10" fill="url(#ornament-gold)"/>

  <!-- Right side panel -->
  <rect class="panel-olive" x="646" y="289" width="188" height="621"/>
  <g class="vents-right">
    <circle class="vent-hole" cx="806" cy="320" r="5"/><circle class="vent-hole" cx="806" cy="346" r="5"/>
    <circle class="vent-hole" cx="806" cy="372" r="5"/><circle class="vent-hole" cx="806" cy="398" r="5"/>
    <circle class="vent-hole" cx="806" cy="425" r="5"/><circle class="vent-hole" cx="806" cy="451" r="5"/>
    <circle class="vent-hole" cx="806" cy="477" r="5"/><circle class="vent-hole" cx="806" cy="504" r="5"/>
    <circle class="vent-hole" cx="806" cy="693" r="5"/><circle class="vent-hole" cx="806" cy="719" r="5"/>
    <circle class="vent-hole" cx="806" cy="746" r="5"/><circle class="vent-hole" cx="806" cy="772" r="5"/>
    <circle class="vent-hole" cx="806" cy="798" r="5"/><circle class="vent-hole" cx="806" cy="825" r="5"/>
    <circle class="vent-hole" cx="806" cy="851" r="5"/><circle class="vent-hole" cx="806" cy="877" r="5"/>
  </g>
  <rect role="img" aria-label="Sunburst medallion with scrolling monogram flourish" x="685" y="308" width="95" height="128" rx="10" fill="url(#ornament-olive)"/>
  <rect role="img" aria-label="Sunburst medallion with scrolling monogram flourish" x="685" y="751" width="95" height="129" rx="10" fill="url(#ornament-olive)"/>
  <g class="side-label" transform="translate(733 608) rotate(-90)">
    <text class="brand brand-ink" x="0" y="16" font-size="50" text-anchor="middle">Corvani</text>
    <text class="small-serif" x="-20" y="-34" font-size="9" fill="var(--ink)" text-anchor="middle" letter-spacing="0.5">SUPERIOR QUALITY</text>
    <text class="small-serif" x="20" y="42" font-size="10" fill="var(--ink)" text-anchor="middle">Since1934</text>
  </g>

  <!-- Bottom flap -->
  <rect class="panel-olive" x="358" y="910" width="288" height="187"/>
  <text class="brand brand-ink" x="502" y="976" font-size="36" text-anchor="middle">Corvani</text>
  <text class="tagline" x="502" y="998" font-size="20" text-anchor="middle">Artisan</text>
  <rect role="img" aria-label="Gold sunburst medallion with scrolling flourishes" x="450" y="1008" width="104" height="51" rx="8" fill="url(#ornament-olive)"/>
</svg>
</body>
</html>
```